Refresh web site from year 2003

Voltaro Forma has a web site (https://vfprosjekt.no/) from early 2000 that needs to be refreshed.

Attached are company logo, favicon files, a licensed image to be used, an animation that illustrate the use of one of the products.

Target Market(s)

Industrial customers

Industry/Entity Type

Electrical Switch Board Builders, Automation Industry

Coding

Coded - Design and coding required

Number of Pages Required

3 page

Requirements
Must have
• WordPress site. Use attached animation in the front page (source file is in Adobe Animation format, if adjustments are needed). Product page for two products, "QRT" and "KV-7 Typ B".
Nice to have
• The site should focus on promoting two products QRT and KV-7 Typ B.

```html
<!DOCTYPE html>
<html lang="en">
<head>
<meta charset="utf-8">
<title>Voltaro Forma</title>
<link href="https://fonts.googleapis.com/css2?family=Roboto:wght@300;400;500;700;900&display=swap" rel="stylesheet">
<style>
:root{
  --navy:#073a75;
  --orange:#f7890c;
  --grey-bg:#eef0f3;
  --ink:#333;
  --footer:#2b2b2b;
  --footer-bar:#1e1e1e;
  --footer-text:#b9b9b9;
  --white:#fff;
}
*{box-sizing:border-box;margin:0;padding:0}
html,body{width:1200px;height:2451px;overflow:hidden}
body{position:relative;font-family:'Roboto',sans-serif;color:var(--ink);background:var(--white)}
.abs{position:absolute}
.backdrop{position:absolute;left:0;top:0}
/* header */
.brand{left:75px;top:26px;font-size:30px;font-weight:700;color:var(--navy)}
.contact-chip{display:flex;align-items:center;top:30px;height:38px;font-size:20px;font-weight:500;color:var(--navy)}
.chip-icon{width:38px;height:38px;border-radius:50%;background:var(--orange);display:flex;align-items:center;justify-content:center;margin-right:7px}
/* nav */
.nav{left:0;top:99px;width:1200px;height:51px;background:var(--navy)}
.nav-item{position:absolute;top:0;height:51px;line-height:51px;font-size:14px;font-weight:700;color:var(--white);text-transform:uppercase}
.nav-item.active{background:var(--orange);width:75px;text-align:center}
.lang{position:absolute;left:1072px;top:16px;display:flex;align-items:center;gap:12px}
/* hero */
.hero{left:0;top:150px;width:1200px;height:573px;background:linear-gradient(100deg,#3e3f41 0%,#7c7d78 30%,#9a9b93 55%,#8a8b84 75%,#5e5f5c 100%);clip-path:polygon(0 0,100% 0,100% 523px,50% 573px,0 523px)}
.hero-shade{position:absolute;inset:0;background:rgba(0,0,0,.28)}
.hero-title{left:0;width:1200px;top:296px;text-align:center;font-size:62px;font-weight:900;color:var(--white)}
.hero-sub{left:140px;width:920px;top:376px;text-align:center;font-size:26px;font-weight:700;line-height:39px;color:var(--white)}
.btn{display:block;text-align:center;background:var(--orange);color:var(--white);font-weight:700;text-transform:uppercase}
.hero-btn{left:507px;top:468px;width:187px;height:43px;line-height:43px;font-size:17px}
.slide-dots{left:566px;top:629px;display:flex;gap:10px}
.slide-dot{width:28px;height:28px;border-radius:50%;background:rgba(255,255,255,.85);display:flex;align-items:center;justify-content:center}
/* about */
.section-title{left:0;width:1200px;text-align:center;font-size:33px;font-weight:700;color:var(--navy)}
.about-text{left:75px;width:1050px;top:838px;text-align:center;font-size:14px;line-height:26.6px;color:var(--ink)}
.about-btn{left:497px;top:946px;width:207px;height:44px;line-height:44px;font-size:14px}
/* services */
.service-card{top:1239px;width:330px;height:206px;border-radius:18px 18px 0 0;background:linear-gradient(180deg,#dedfe3 0%,#eef0f3 60%,#f7f8f9 100%)}
.service-icon{position:absolute;left:50%;top:-54px;margin-left:-61px;width:122px;height:122px;border-radius:50%;background:#35373b;border:4px solid #e8e9ec;display:flex;align-items:center;justify-content:center}
.service-name{position:absolute;left:0;width:100%;top:80px;text-align:center;font-size:25px;font-weight:700;color:var(--navy)}
.service-desc{position:absolute;left:15px;width:300px;top:124px;text-align:center;font-size:14.5px;line-height:25px;color:var(--ink)}
/* products */
.products-title{color:var(--white);top:1600px}
.product{top:1677px;width:332px}
.product-photo{width:332px;height:181px;border:5px solid var(--white);background:linear-gradient(135deg,#a9aaa6 0%,#8e8f8b 50%,#c2c3bf 100%)}
.product-name{margin-top:17px;text-align:center;font-size:22px;font-weight:500;line-height:29px;color:var(--white)}
.product-desc{margin-top:9px;text-align:center;font-size:14.5px;line-height:24px;font-weight:300;color:#dfe6f0}
.carousel-arrow{top:1796px}
/* footer */
.footer{left:0;top:2107px;width:1200px;height:289px;background:var(--footer)}
.footer-bar{left:0;top:2396px;width:1200px;height:55px;background:var(--footer-bar);color:var(--white);font-size:12px;text-align:center;line-height:55px}
.footer-brand{left:75px;top:2172px;font-size:28px;font-weight:700;color:var(--white)}
.footer-about{left:75px;top:2250px;width:250px;font-size:14px;line-height:23px;color:var(--footer-text)}
.footer-col{top:2152px}
.footer-head{font-size:14px;font-weight:500;color:var(--white);padding-bottom:10px;border-bottom:1px solid #4a4a4a;width:192px}
.footer-list{list-style:none;margin-top:13px}
.footer-list li{font-size:13px;color:var(--footer-text);height:34.2px;display:flex;align-items:flex-start;gap:10px}
.social-box{width:11px;height:11px;background:var(--footer-text);border-radius:2px;margin-top:3px}
.footer-divider{top:2152px;width:1px;height:210px;background:#3a3a3a}
.contact-row{position:absolute;left:0;display:flex;gap:22px;font-size:13px;color:var(--footer-text);line-height:21px}
.contact-row .ico{width:11px;margin-top:4px}
.accent{color:var(--orange);font-weight:500}
.strong{color:var(--white);font-weight:500}
</style>
</head>
<body>

<svg class="backdrop" width="1200" height="2451" aria-hidden="true">
  <polygon points="0,1104 600,1053 1200,1104 1200,1480 0,1480" fill="#eef0f3"/>
  <polygon points="0,1475 600,1534 1200,1475 1200,2107 0,2107" fill="#073a75"/>
</svg>

<!-- header -->
<div class="abs brand">Voltaro Forma</div>
<div class="abs contact-chip" style="left:684px">
  <span class="chip-icon"><svg width="18" height="18" viewBox="0 0 24 24"><path fill="#fff" d="M6.6 10.8a15 15 0 0 0 6.6 6.6l2.2-2.2a1 1 0 0 1 1-.25 11.4 11.4 0 0 0 3.6.6 1 1 0 0 1 1 1V20a1 1 0 0 1-1 1A17 17 0 0 1 3 4a1 1 0 0 1 1-1h3.5a1 1 0 0 1 1 1c0 1.25.2 2.45.6 3.6a1 1 0 0 1-.25 1z"/></svg></span>
  +47 921 40 718
</div>
<div class="abs contact-chip" style="left:891px">
  <span class="chip-icon"><svg width="18" height="14" viewBox="0 0 18 14"><rect x="1" y="1" width="16" height="12" rx="1.5" fill="none" stroke="#fff" stroke-width="2"/><path d="M1.5 2l7.5 6 7.5-6" fill="none" stroke="#fff" stroke-width="2"/></svg></span>
  post@vfprosjekt.no
</div>

<!-- navigation -->
<nav class="abs nav">
  <span class="nav-item active" style="left:75px">Home</span>
  <span class="nav-item" style="left:186px">Products</span>
  <span class="nav-item" style="left:313px">Services</span>
  <span class="nav-item" style="left:432px">About</span>
  <span class="nav-item" style="left:532px">Contact</span>
  <span class="lang">
    <svg width="30" height="20" viewBox="0 0 30 20"><rect width="30" height="20" fill="#012169"/><path d="M0 0L30 20M30 0L0 20" stroke="#fff" stroke-width="4"/><path d="M0 0L30 20M30 0L0 20" stroke="#c8102e" stroke-width="1.5"/><path d="M15 0V20M0 10H30" stroke="#fff" stroke-width="6"/><path d="M15 0V20M0 10H30" stroke="#c8102e" stroke-width="3"/></svg>
    <svg width="12" height="8" viewBox="0 0 12 8"><path d="M1 1l5 5 5-5" fill="none" stroke="#fff" stroke-width="1.6"/></svg>
  </span>
</nav>

<!-- hero -->
<div class="abs hero" role="img" aria-label="Photo of industrial switchboard cabinets with indicator lamps and rotary switches"><div class="hero-shade"></div></div>
<h1 class="abs hero-title">Welcome to Voltaro Forma</h1>
<p class="abs hero-sub">Voltaro Forma is a production and development company for electronics with emphasis on small series production.</p>
<a class="abs btn hero-btn">Read More</a>
<div class="abs slide-dots">
  <span class="slide-dot"><svg width="12" height="12" viewBox="0 0 12 12"><path d="M8 1L3 6l5 5" fill="none" stroke="#555" stroke-width="2.4"/></svg></span>
  <span class="slide-dot"><svg width="12" height="12" viewBox="0 0 12 12"><path d="M4 1l5 5-5 5" fill="none" stroke="#555" stroke-width="2.4"/></svg></span>
</div>

<!-- about -->
<h2 class="abs section-title" style="top:784px">About Voltaro Forma</h2>
<p class="abs about-text">Voltaro Forma is a production and development company for electronics with emphasis on small series production. We are today two employees with good and relevant access to additional expertise in the established network. The company was established in 1985 and has since 2001 taken over production equipment and production basis from another company in the same industry.</p>
<a class="abs btn about-btn">More About Company</a>

<!-- services -->
<h2 class="abs section-title" style="top:1110px">Services</h2>
<div class="abs service-card" style="left:75px">
  <div class="service-icon"><svg width="56" height="50" viewBox="0 0 56 50" fill="none" stroke="#fff" stroke-width="2"><circle cx="20" cy="22" r="11"/><circle cx="20" cy="22" r="4"/><circle cx="40" cy="14" r="7"/><circle cx="40" cy="14" r="2.5"/><circle cx="40" cy="36" r="7"/><circle cx="40" cy="36" r="2.5"/><path d="M20 7v4M20 33v4M5 22h4M31 22h4M40 3v4M40 21v4M40 25v4M40 43v4"/></svg></div>
  <div class="service-name">Production</div>
  <div class="service-desc">Small series production of electronic units in the number of 10 to 200 units.</div>
</div>
<div class="abs service-card" style="left:436px">
  <div class="service-icon"><svg width="58" height="54" viewBox="0 0 58 54" fill="none" stroke="#fff" stroke-width="2"><rect x="6" y="12" width="46" height="32" rx="2"/><path d="M2 48h54"/><circle cx="29" cy="14" r="7"/><circle cx="29" cy="14" r="2.5"/><circle cx="20" cy="34" r="4"/><path d="M14 42c0-4 3-6 6-6s6 2 6 6M32 32h14M32 38h10"/></svg></div>
  <div class="service-name">Devolopment</div>
  <div class="service-desc">Development of product concept to finished product in collaboration with a customer.</div>
</div>
<div class="abs service-card" style="left:795px">
  <div class="service-icon"><svg width="60" height="40" viewBox="0 0 60 40" fill="none" stroke="#fff" stroke-width="2.2"><rect x="10" y="3" width="40" height="27" rx="2"/><rect x="15" y="8" width="30" height="17"/><path d="M2 33h56l-3 4H5z"/></svg></div>
  <div class="service-name">Design</div>
  <div class="service-desc">Designing of electronics and print cards for pre-assembled and tested unit.</div>
</div>

<!-- products -->
<h2 class="abs section-title products-title">Our Products</h2>
<svg class="abs carousel-arrow" style="left:45px" width="16" height="28" viewBox="0 0 16 28"><path d="M14 2L3 14l11 12" fill="none" stroke="#fff" stroke-width="2"/></svg>
<svg class="abs carousel-arrow" style="left:1140px" width="16" height="28" viewBox="0 0 16 28"><path d="M2 2l11 12L2 26" fill="none" stroke="#fff" stroke-width="2"/></svg>

<div class="abs product" style="left:75px">
  <div class="product-photo" role="img" aria-label="Photo of a panel of signal lamps in red, green and orange being pressed"></div>
  <div class="product-name">Signal Lamp<br>with built-in LED</div>
  <div class="product-desc">Duis aliquam nibh a dui iaculis viverra id a velit. Vivamus egestas risus in magna varius commodosemper viverra egestas.</div>
</div>
<div class="abs product" style="left:437px">
  <div class="product-photo" role="img" aria-label="Photo of electrical switch indicators with red and green LED rows"></div>
  <div class="product-name">Electrical Swith Indicator<br>with built-in LED rows</div>
  <div class="product-desc">Duis aliquam nibh a dui iaculis viverra id a velit. Vivamus egestas risus in magna varius commodosemper viverra egestas.</div>
</div>
<div class="abs product" style="left:794px">
  <div class="product-photo" role="img" aria-label="Photo of measurement value converters mounted on a grey cabinet wall"></div>
  <div class="product-name">Measurement Value<br>Converters</div>
  <div class="product-desc">Duis aliquam nibh a dui iaculis viverra id a velit. Vivamus egestas risus in magna varius commodosemper viverra egestas.</div>
</div>

<!-- footer -->
<footer class="abs footer"></footer>
<div class="abs footer-brand">Voltaro Forma</div>
<p class="abs footer-about">Duis aliquam nibh a dui iaculis viverra id a velit. Vivamus egestas risus in magna varius commodo semper viverra egestas.</p>

<div class="abs footer-divider" style="left:352px"></div>
<div class="abs footer-divider" style="left:609px"></div>
<div class="abs footer-divider" style="left:868px"></div>

<div class="abs footer-col" style="left:384px">
  <div class="footer-head">SITE MAP</div>
  <ul class="footer-list">
    <li>Home</li><li>Products</li><li>Services</li><li>About</li><li>Contact</li>
  </ul>
</div>
<div class="abs footer-col" style="left:646px">
  <div class="footer-head" style="width:190px">FOLLOW US</div>
  <ul class="footer-list">
    <li><span class="social-box"></span>Fjordbook</li>
    <li><span class="social-box"></span>Chirper</li>
    <li><span class="social-box"></span>WorkLink</li>
    <li><span class="social-box"></span>Searchly +</li>
    <li><span class="social-box"></span>ClipTube</li>
  </ul>
</div>
<div class="abs footer-col" style="left:903px;width:200px;height:200px">
  <div class="footer-head">CONTACT US</div>
  <div class="contact-row" style="top:44px">
    <svg class="ico" width="11" height="13" viewBox="0 0 11 14"><path d="M5.5 0A5 5 0 0 0 .5 5c0 4 5 9 5 9s5-5 5-9a5 5 0 0 0-5-5z" fill="#b9b9b9"/><circle cx="5.5" cy="5" r="2" fill="#2b2b2b"/></svg>
    <div><span class="accent">VOLTARO FORMA</span><br>Brekkevegen 42<br>N-4710 Heldal Norway</div>
  </div>
  <div class="contact-row" style="top:112px">
    <svg class="ico" width="11" height="11" viewBox="0 0 24 24"><path fill="#b9b9b9" d="M6.6 10.8a15 15 0 0 0 6.6 6.6l2.2-2.2a1 1 0 0 1 1-.25 11.4 11.4 0 0 0 3.6.6 1 1 0 0 1 1 1V20a1 1 0 0 1-1 1A17 17 0 0 1 3 4a1 1 0 0 1 1-1h3.5a1 1 0 0 1 1 1c0 1.25.2 2.45.6 3.6a1 1 0 0 1-.25 1z"/></svg>
    <span class="strong">+47 921 40 718</span>
  </div>
  <div class="contact-row" style="top:142px">
    <svg class="ico" width="12" height="10" viewBox="0 0 18 14"><rect x="1" y="1" width="16" height="12" fill="none" stroke="#b9b9b9" stroke-width="2"/><path d="M1.5 2l7.5 6 7.5-6" fill="none" stroke="#b9b9b9" stroke-width="2"/></svg>
    <span class="strong">post@vfprosjekt.no</span>
  </div>
</div>

<div class="abs footer-bar">Copyright © 2022. Company Name. All Right Reserved</div>

</body>
</html>
```